Local Roofing/Construction company business needs new biz card design

We need a new business card design, current cards are from the start of this operation and generic at best. We are a local Construction Company (General Contractor) with a majority of our work originating from insurance claims-exterior finish work is the main focus (Roofs-Siding-Gutters etc). Heavily involved with homeowners and the low ball offers they receive from insurance company's after a insurable event takes place. I have attached some of our original logo file(s) below.

```html
<!DOCTYPE html>
<html lang="en">
<head>
<meta charset="utf-8">
<title>Ridgeline Construction – Business Card</title>
<link href="https://fonts.googleapis.com/css2?family=Montserrat:wght@700&family=Poppins:wght@400;700&display=swap" rel="stylesheet">
<style>
  :root {
    --green: #33d77f;
    --green-deep: #27c06c;
    --ink: #1d1d1d;
    --muted: #3a3a3a;
    --swoosh: #e3e4e6;
    --paper: #ffffff;
    --backdrop: #eef0ef;
  }
  * { box-sizing: border-box; margin: 0; padding: 0; }
  html, body { width: 1200px; height: 900px; overflow: hidden; }
  body {
    background: var(--backdrop);
    font-family: "Poppins", sans-serif;
    display: flex;
    flex-direction: column;
    align-items: center;
    justify-content: center;
    gap: 56px;
  }
  .card {
    position: relative;
    width: 630px;
    height: 360px;
    overflow: hidden;
    box-shadow: 0 8px 22px rgba(0,0,0,0.14);
  }

  /* Back side */
  .card-back { background: var(--green); }
  .card-back .pattern-area {
    position: absolute; inset: 0;
    background: linear-gradient(135deg, var(--green) 0%, var(--green-deep) 100%);
  }
  .card-back .brand-badge {
    position: absolute;
    right: 70px; top: 150px;
    display: flex; align-items: center; gap: 10px;
    color: var(--paper);
    font-family: "Poppins", sans-serif;
    font-weight: 700;
    font-size: 18px;
    letter-spacing: 0.04em;
    line-height: 1.1;
  }
  .brand-square { width: 16px; height: 16px; background: currentColor; flex: none; }

  /* Front side */
  .card-front { background: var(--paper); }
  .card-front .waves { position: absolute; inset: 0; width: 100%; height: 100%; }
  .card-front .brand {
    position: absolute;
    right: 44px; top: 50px;
    display: flex; align-items: center; gap: 10px;
    color: var(--green);
    font-family: "Poppins", sans-serif;
    font-weight: 700;
    font-size: 22px;
    letter-spacing: 0.04em;
    line-height: 1.1;
  }
  .card-front .person { position: absolute; left: 52px; top: 78px; }
  .person-name {
    font-family: "Montserrat", sans-serif;
    font-weight: 700;
    font-size: 27px;
    color: var(--green);
    letter-spacing: 0.02em;
    line-height: 1;
  }
  .person-title {
    font-size: 17px;
    color: var(--muted);
    margin-top: 4px;
    letter-spacing: 0.02em;
  }
  .card-front .contact {
    position: absolute; left: 72px; top: 170px;
    font-size: 16px; color: var(--ink);
    line-height: 1.45;
  }
  .contact-row { display: flex; align-items: center; gap: 10px; }
  .contact-row svg { width: 18px; height: 18px; flex: none; }
  .contact-address { margin-top: 12px; padding-left: 0; }
  .card-front .website {
    position: absolute; right: 34px; bottom: 30px;
    color: var(--paper); font-size: 15px; letter-spacing: 0.02em;
  }
</style>
</head>
<body>

  <section class="card card-back">
    <div class="pattern-area" role="img" aria-label="Repeating pattern of the company brand mark in darker green tiles"></div>
    <div class="brand-badge">
      <span class="brand-square"></span>
      <span>RIDGELINE<br>CONSTRUCTION</span>
    </div>
  </section>

  <section class="card card-front">
    <svg class="waves" viewBox="0 0 630 360" preserveAspectRatio="none" aria-hidden="true">
      <path d="M0,292 C190,302 360,278 460,200 C520,152 580,122 630,110 L630,360 L0,360 Z" fill="var(--swoosh)"/>
      <path d="M0,318 C200,326 380,300 480,222 C540,176 590,150 630,138 L630,360 L0,360 Z" fill="var(--green)"/>
    </svg>

    <div class="brand">
      <span class="brand-square"></span>
      <span>RIDGELINE<br>CONSTRUCTION</span>
    </div>

    <div class="person">
      <h1 class="person-name">DANIEL HARPER</h1>
      <p class="person-title">Managing Director</p>
    </div>

    <div class="contact">
      <div class="contact-row">
        <svg viewBox="0 0 24 24" aria-hidden="true"><path fill="var(--green)" d="M6.6 10.8a15.1 15.1 0 0 0 6.6 6.6l2.2-2.2a1 1 0 0 1 1-.25 11.4 11.4 0 0 0 3.6.57 1 1 0 0 1 1 1V20a1 1 0 0 1-1 1A17 17 0 0 1 3 4a1 1 0 0 1 1-1h3.5a1 1 0 0 1 1 1c0 1.25.2 2.45.57 3.6a1 1 0 0 1-.25 1z"/></svg>
        <span>044-987 654 321</span>
      </div>
      <div class="contact-row">
        <svg viewBox="0 0 24 24" aria-hidden="true"><rect x="2" y="5" width="20" height="14" fill="var(--green)"/><path d="M2 5l10 8 10-8" fill="none" stroke="#fff" stroke-width="1.8"/></svg>
        <span>info@ridgelinebuild.com</span>
      </div>
      <p class="contact-address">118, Quarry Lane<br>Millbrook, 45210</p>
    </div>

    <p class="website">www.ridgelinebuild.com</p>
  </section>

</body>
</html>
```